Communication and Marketing agency needs a new presentation card

We are a group of communication and marketing agencies specialized in companies that are in the logistics and industrial sector. The head agency is TELVANO Grupo and the group consists of 4 agencies: TELVANO Media, TELVANO Digital, TELVANO Research and EnlazaPorImagen. We hace 4 offices in Spain (Madrid, Barcelona, Valencia and Murcia). We are looking for a clean and attractive design that transmits our experience, brand presence in the market and knowledge to those who receive the card.It has to maintain the colors of the logo that is attached.
Target Market(s)
logistics and industrial sector
Marketing department
Clean and attractive design

```html
<!DOCTYPE html>
<html lang="en">
<head>
<meta charset="UTF-8">
<title>TELVANO Grupo – Business Card</title>
<link href="https://fonts.googleapis.com/css2?family=Oswald:wght@400;500&family=Open+Sans:wght@400&display=swap" rel="stylesheet">
<style>
  :root {
    --backdrop: #5e4432;
    --card: #202020;
    --rule: #343434;
    --silver: #8d8d8d;
    --silver-light: #a9a9a9;
    --grey-text: #9a9a9a;
    --red: #c4202b;
  }
  * { margin: 0; padding: 0; box-sizing: border-box; }
  html, body { width: 1200px; height: 1000px; overflow: hidden; }
  body {
    background: var(--backdrop);
    position: relative;
    font-family: "Open Sans", Arial, sans-serif;
  }
  .card {
    position: absolute;
    left: 266px;
    width: 666px;
    height: 397px;
    background: var(--card);
  }
  .card--front { top: 74px; }
  .card--back { top: 534px; }

  .brand-main {
    position: absolute;
    top: 132px;
    left: 0;
    width: 100%;
    text-align: center;
    font-family: "Oswald", Arial, sans-serif;
    font-weight: 400;
    font-size: 66px;
    letter-spacing: 4px;
    color: var(--silver-light);
    line-height: 1;
  }
  .divider {
    position: absolute;
    top: 299px;
    left: 62px;
    width: 542px;
    height: 1px;
    background: var(--rule);
  }
  .agency-list {
    position: absolute;
    top: 332px;
    left: 40px;
    width: 586px;
    display: flex;
    justify-content: space-between;
    align-items: center;
    list-style: none;
  }
  .agency {
    width: 180px;
    text-align: center;
    font-family: "Oswald", Arial, sans-serif;
    font-weight: 400;
    font-size: 18px;
    color: var(--silver);
    letter-spacing: 0.5px;
  }
  .agency--feature { color: var(--red); }

  .contact-block {
    position: absolute;
    top: 166px;
    left: 0;
    width: 100%;
  }
  .person {
    position: absolute;
    right: 364px;
    top: 0;
    text-align: right;
  }
  .person__name {
    font-family: "Oswald", Arial, sans-serif;
    font-weight: 500;
    font-size: 22px;
    color: var(--red);
    letter-spacing: 0.5px;
    line-height: 26px;
  }
  .person__role {
    font-size: 15px;
    color: var(--grey-text);
    line-height: 22px;
  }
  .contact-rule {
    position: absolute;
    left: 321px;
    top: 4px;
    width: 1px;
    height: 40px;
    background: var(--red);
  }
  .contact-lines {
    position: absolute;
    left: 338px;
    top: 2px;
    list-style: none;
  }
  .contact-lines li {
    display: flex;
    align-items: center;
    gap: 6px;
    font-size: 15px;
    color: var(--grey-text);
    line-height: 23px;
  }
  .contact-lines svg { width: 12px; height: 12px; fill: var(--red); }
  .address {
    position: absolute;
    top: 347px;
    left: 0;
    width: 100%;
    text-align: center;
    font-size: 15.5px;
    color: #858585;
  }
</style>
</head>
<body>
  <section class="card card--front" aria-label="Card front">
    <h1 class="brand-main">TELVANO Grupo</h1>
    <div class="divider"></div>
    <ul class="agency-list">
      <li class="agency">TELVANO Research</li>
      <li class="agency agency--feature">EnlazaPorImagen</li>
      <li class="agency">TELVANO Digital</li>
    </ul>
  </section>

  <section class="card card--back" aria-label="Card back">
    <div class="contact-block">
      <div class="person">
        <p class="person__name">DARREN L. WHITCOMBE</p>
        <p class="person__role">Founder</p>
      </div>
      <div class="contact-rule"></div>
      <ul class="contact-lines">
        <li>
          <svg viewBox="0 0 24 24" aria-hidden="true"><path d="M3 9c0-3 4-5 9-5s9 2 9 5v2h-5V8.5c-2-.7-6-.7-8 0V11H3zM6 13h12l2 7H4z"/></svg>
          (646) 555-0187
        </li>
        <li>
          <svg viewBox="0 0 24 24" aria-hidden="true"><path d="M2 5h20v2l-10 6L2 7zM2 9.3l10 6 10-6V19H2z"/></svg>
          dw@harborlinecap.com
        </li>
      </ul>
    </div>
    <p class="address">410 Madison Avenue 18th Floor, New York, NY 10017</p>
  </section>
</body>
</html>
```